Dravel

We are openıng one huntıng showroom in Riyadh? Saudi Arabia. Company name is "DRAVEL".
Our logo designed and we need Business Card Design now.
I attached DRAVEL logo below.
Front side will English and back side will be Arabic

```html
<!DOCTYPE html>
<html lang="en">
<head>
<meta charset="utf-8">
<title>Dravel — Business Card</title>
<link href="https://fonts.googleapis.com/css2?family=Open+Sans:wght@400;600;700;800&family=Noto+Sans+Arabic:wght@400;700&display=swap" rel="stylesheet">
<style>
  :root {
    --forest: #07793f;
    --leaf: #7aa843;
    --paper: #ffffff;
    --backdrop: #2b2b2b;
    --ink-light: #ffffff;
  }
  * { box-sizing: border-box; margin: 0; padding: 0; }
  html, body { width: 1200px; height: 892px; overflow: hidden; }
  body {
    background: var(--backdrop);
    font-family: "Open Sans", Arial, sans-serif;
    position: relative;
  }
  .card {
    position: absolute;
    width: 630px;
    height: 360px;
    display: flex;
    background: var(--paper);
    box-shadow: 0 12px 30px rgba(0,0,0,.45);
  }
  .card--back  { left: 150px; top: 70px; }
  .card--front { left: 420px; top: 462px; }

  .card__edge { width: 14px; flex: none; }
  .card__brand {
    width: 266px;
    flex: none;
    display: flex;
    align-items: center;
    justify-content: center;
  }
  .brand-name {
    font-weight: 800;
    font-size: 54px;
    letter-spacing: 1px;
    color: var(--forest);
  }
  .card__panel {
    flex: 1;
    color: var(--ink-light);
    padding: 44px 40px 36px 44px;
    display: flex;
    flex-direction: column;
    justify-content: space-between;
  }
  .card--back .card__edge  { background: var(--forest); }
  .card--back .card__panel { background: var(--leaf); }
  .card--front .card__edge  { background: var(--leaf); }
  .card--front .card__panel { background: var(--forest); }

  .holder__name { font-weight: 700; font-size: 21px; line-height: 1.1; }
  .holder__role { font-size: 14px; line-height: 1.3; }

  .contact { font-size: 14.5px; line-height: 1.5; }
  .contact__address { margin-bottom: 8px; }
  .contact__line { display: flex; align-items: center; gap: 10px; }
  .contact__line svg { width: 14px; height: 14px; fill: var(--ink-light); flex: none; }

  .card--back .card__panel { font-family: "Noto Sans Arabic", "Open Sans", sans-serif; }
  .card--back .holder,
  .card--back .contact__address { direction: rtl; text-align: left; }
  .card--back .holder__name { font-size: 22px; }
</style>
</head>
<body>

<svg width="0" height="0" style="position:absolute" aria-hidden="true">
  <symbol id="icon-phone" viewBox="0 0 16 16"><path d="M2 5c0-2 3-3 6-3s6 1 6 3v1h-3V5H5v1H2z"/><path d="M4 7h8l2 6H2z"/></symbol>
  <symbol id="icon-mobile" viewBox="0 0 16 16"><path d="M4 1h8v14H4zM5.5 3v9h5V3z"/></symbol>
  <symbol id="icon-fax" viewBox="0 0 16 16"><path d="M4 1h8v5H4z"/><path d="M1 7h14v6h-3v2H4v-2H1zM5 11v3h6v-3z"/></symbol>
  <symbol id="icon-mail" viewBox="0 0 16 16"><path d="M1 3h14v10H1zM2.5 4.5 8 9l5.5-4.5z"/></symbol>
  <symbol id="icon-web" viewBox="0 0 16 16"><path d="M8 1a7 7 0 1 0 0 14A7 7 0 0 0 8 1zm0 2a5 5 0 0 1 3 9L6 4a5 5 0 0 1 2-1z"/></symbol>
</svg>

<section class="card card--back" lang="ar">
  <div class="card__edge"></div>
  <div class="card__brand"><span class="brand-name" lang="en">DRAVEL</span></div>
  <div class="card__panel">
    <div class="holder">
      <p class="holder__name">كريم ناصر</p>
      <p class="holder__role">رئيس</p>
    </div>
    <div class="contact">
      <p class="contact__address">٢٧ شارع العليا<br>الرياض ١٢٢١١</p>
      <p class="contact__line"><svg><use href="#icon-phone"/></svg>555 0142 7781</p>
      <p class="contact__line"><svg><use href="#icon-mobile"/></svg>555 0198 3364</p>
      <p class="contact__line"><svg><use href="#icon-fax"/></svg>555 0127 9150</p>
      <p class="contact__line"><svg><use href="#icon-mail"/></svg>info@dravel.com</p>
      <p class="contact__line"><svg><use href="#icon-web"/></svg>www.dravel.com</p>
    </div>
  </div>
</section>

<section class="card card--front">
  <div class="card__edge"></div>
  <div class="card__brand"><span class="brand-name">DRAVEL</span></div>
  <div class="card__panel">
    <div class="holder">
      <p class="holder__name">KARIM NASSER</p>
      <p class="holder__role">PRESIDENT</p>
    </div>
    <div class="contact">
      <p class="contact__address">27 Olaya Street<br>Riyadh 12211</p>
      <p class="contact__line"><svg><use href="#icon-phone"/></svg>555 0142 7781</p>
      <p class="contact__line"><svg><use href="#icon-mobile"/></svg>555 0198 3364</p>
      <p class="contact__line"><svg><use href="#icon-fax"/></svg>555 0127 9150</p>
      <p class="contact__line"><svg><use href="#icon-mail"/></svg>info@dravel.com</p>
      <p class="contact__line"><svg><use href="#icon-web"/></svg>www.dravel.com</p>
    </div>
  </div>
</section>

</body>
</html>
```